Landing Page for Bathroom Remodeling Webpage - Desktop and Mobile

I am looking for some help designing the "above the fold" area for my bathroom remodeling service page. Looking for something a little different than the rest. Typically remodeling companies just put a nice picture of a bathroom remodel but I would like to do something a little different / more creative. Below is a link to the current wireframe we are working on.
Current website is located at plumvantaridge.com
Again the biggest thing I am looking for is a design for the very top section but would love help on the rest of the page as well. You will see by viewing the link below the type of information we are looking to include on the page:
PLEASE DO INCLUDE WHAT THE MOBILE VERSION WOULD LOOK LIKE AS WELL.
Wireframe:
https://boards.quillmerra.com/view/3f8a1b2c-90de-4e7a-b5c1-aa62d09e1f35-418k/
There are also comments in the link above you can read as well.
We like the idea of something interactive such as this...
https://pixorvale.com/shots/5192746-Glenhart-Scooter-Store-Animation
Attached is also the logo we want to use going forward
Target Market(s)
Residential homeowners, 30 years old+ with professional careers
Number of Pages Required
1 page
Look and feel
Each slider illustrates characteristics of the customer's brand and the style your logo design should communicate.

```html
<!DOCTYPE html>
<html lang="en">
<head>
<meta charset="utf-8">
<title>Dwellcraft – Bathroom Remodeling</title>
<link rel="stylesheet" href="https://fonts.googleapis.com/css2?family=Playfair+Display:wght@400;700&family=Roboto:wght@400;500;700;900&display=swap">
<style>
  :root {
    --red: #d0201f;
    --navy: #183463;
    --navy-deep: #10284f;
    --card-navy: #21406f;
    --ink: #2d2d2d;
    --white: #ffffff;
    --photo-warm: #b89a7c;
    --photo-stone: #ddd6cc;
  }
  * { box-sizing: border-box; margin: 0; padding: 0; }
  html, body { width: 1200px; height: 3524px; overflow: hidden; background: var(--white); }
  body { position: relative; font-family: "Roboto", sans-serif; color: var(--ink); }
  .abs { position: absolute; }

  .site-header { left: 0; top: 0; width: 1200px; height: 228px; }
  .brand { left: 52px; top: 70px; display: flex; align-items: center; gap: 22px; }
  .brand-mark { width: 60px; height: 60px; background: var(--red); }
  .brand-name { font-family: "Roboto", sans-serif; font-weight: 900; font-size: 76px; color: var(--navy); letter-spacing: 1px; line-height: 1; }
  .menu-toggle { left: 1044px; top: 56px; width: 112px; height: 104px; }

  .band { left: 0; width: 1200px; height: 220px; display: flex; align-items: center; justify-content: center;
    font-family: "Playfair Display", serif; color: var(--white); font-size: 58px; letter-spacing: 1px; }
  .band-estimate { top: 228px; background: var(--red); }
  .band-consult { top: 468px; background: var(--navy); }

  .section-title { left: 0; width: 1200px; text-align: center; font-family: "Playfair Display", serif; color: var(--navy); line-height: 1.1; }
  .section-title .accent { color: var(--red); }
  .inspired { top: 732px; font-size: 60px; }

  .photo { border: none; }
  .photo-side-left { left: 0; top: 912px; width: 240px; height: 428px; background: linear-gradient(90deg, #e9e3da, #c8b8a3); }
  .photo-main { left: 280px; top: 880px; width: 672px; height: 480px; background: linear-gradient(180deg, #6f7f5a 0%, #a7a28f 45%, #8c6a4c 75%, #3a2e27 100%); }
  .photo-side-right { left: 1000px; top: 912px; width: 200px; height: 428px; background: linear-gradient(90deg, var(--photo-stone), var(--photo-warm)); }

  .btn-explore { left: 512px; top: 1452px; width: 340px; height: 136px; background: var(--red); color: var(--white);
    font-family: "Playfair Display", serif; font-size: 40px; display: flex; align-items: center; justify-content: center; letter-spacing: 1px; }

  .simple { top: 1640px; font-size: 68px; }
  .intro { left: 120px; top: 1736px; width: 960px; text-align: center; font-size: 28px; line-height: 40px; color: #3a3a3a; }

  .materials { top: 2060px; font-size: 56px; }
  .materials-sub { left: 140px; top: 2140px; width: 920px; text-align: center; font-size: 28px; line-height: 40px; color: #3a3a3a; }

  .material { top: 2270px; width: 300px; text-align: center; }
  .material svg { display: block; margin: 0 auto; width: 230px; height: 240px; }
  .material-label { margin-top: 38px; font-weight: 500; font-size: 32px; letter-spacing: 1px; color: var(--red); }

  .pricing { top: 2628px; font-size: 56px; }

  .package { color: var(--white); text-align: center; }
  .package-minor, .package-major { top: 2852px; width: 316px; height: 552px; background: var(--card-navy); }
  .package-minor { left: 56px; }
  .package-major { left: 828px; }
  .package-moderate { left: 380px; top: 2760px; width: 440px; height: 648px; background: var(--red);
    box-shadow: 0 8px 24px rgba(0,0,0,.25); }
  .package-name { font-weight: 700; letter-spacing: 1px; }
  .package-minor .package-name, .package-major .package-name { margin-top: 28px; font-size: 30px; }
  .package-moderate .package-name { margin-top: 32px; font-size: 42px; }
  .package-desc { margin: 8px auto 0; font-size: 20px; line-height: 24px; width: 260px; }
  .package-moderate .package-desc { font-size: 26px; line-height: 30px; width: 380px; }
  .features { list-style: none; text-align: left; }
  .package-minor .features, .package-major .features { margin: 56px 0 0 40px; font-size: 20px; line-height: 28px; }
  .package-moderate .features { margin: 52px 0 0 40px; font-size: 28px; line-height: 36px; }
  .features li { display: flex; align-items: center; gap: 14px; }
  .features li.excluded { opacity: .35; }
  .features svg { width: .8em; height: .8em; flex: none; }
  .best-value { left: 692px; top: 3370px; width: 160px; height: 72px; background: var(--navy-deep); color: var(--white);
    font-weight: 700; font-size: 20px; display: flex; align-items: center; justify-content: center; transform: rotate(-24deg); letter-spacing: 1px; }
</style>
</head>
<body>
  <header class="site-header abs">
    <div class="brand abs">
      <span class="brand-mark"></span>
      <span class="brand-name">DWELLCRAFT</span>
    </div>
    <svg class="menu-toggle abs" viewBox="0 0 112 104" aria-label="Menu">
      <rect x="0" y="8" width="112" height="20" rx="10" fill="var(--navy)"/>
      <rect x="0" y="42" width="112" height="20" rx="10" fill="var(--navy)"/>
      <rect x="0" y="76" width="112" height="20" rx="10" fill="var(--navy)"/>
    </svg>
  </header>

  <div class="band band-estimate abs">GET AN ESTIMATE: 555-014-2368</div>
  <div class="band band-consult abs">SCHEDULE A FREE CONSULTATION</div>

  <h2 class="section-title inspired abs"><span class="accent">Get inspired</span> by similar projects.</h2>

  <div class="photo photo-side-left abs" role="img" aria-label="Finished bathroom with freestanding tub and light tile"></div>
  <div class="photo photo-main abs" role="img" aria-label="Remodeled bathroom with large windows, soaking tub and dark wood vanity"></div>
  <div class="photo photo-side-right abs" role="img" aria-label="Bathroom with copper soaking tub and stone walls"></div>

  <a class="btn-explore abs">EXPLORE</a>

  <h2 class="section-title simple abs">Bathroom remodeling made <span class="accent">simple.</span></h2>
  <p class="intro abs">Bathroom remodel can be complex, but when completed in an eco-friendly and sustainable manner can also drastically decrease monthly bills and give you the satisfaction of reducing your carbon footprint in the process. A bathroom remodel ranges anywhere from updating your plumbing fixture, to making more efficient use of the space, to building the in-home spa of your dreams. A bathroom remodel is subjective, but homeowners are generally faced with the same universal challenges regardless of project scope.</p>

  <h2 class="section-title materials abs">Material Selections</h2>
  <p class="materials-sub abs">For your bathroom remodel there will be material selections you will have to make. Use the lists below to get an idea of some of the options.</p>

  <div class="material abs" style="left:0">
    <svg viewBox="0 0 230 240" aria-hidden="true">
      <circle cx="115" cy="92" r="88" fill="var(--navy)"/>
      <rect x="72" y="150" width="86" height="70" fill="var(--navy)"/>
      <rect x="82" y="222" width="66" height="18" rx="6" fill="var(--navy)"/>
      <path d="M90 70 h50 v26 h-14 v60 h-22 v-60 h-14 z" fill="var(--white)"/>
    </svg>
    <div class="material-label">ELECTRICAL</div>
  </div>
  <div class="material abs" style="left:300px">
    <svg viewBox="0 0 230 240" aria-hidden="true">
      <path d="M40 240 V70 a60 60 0 0 1 120 0" fill="none" stroke="var(--navy)" stroke-width="24"/>
      <path d="M100 96 a64 64 0 0 1 124 0 z" fill="var(--navy)"/>
      <g fill="var(--navy)">
        <circle cx="130" cy="124" r="7"/><circle cx="162" cy="124" r="7"/><circle cx="194" cy="124" r="7"/>
        <circle cx="118" cy="152" r="7"/><circle cx="150" cy="152" r="7"/><circle cx="182" cy="152" r="7"/><circle cx="212" cy="152" r="7"/>
        <circle cx="134" cy="180" r="7"/><circle cx="166" cy="180" r="7"/><circle cx="198" cy="180" r="7"/>
      </g>
    </svg>
    <div class="material-label">PLUMBING</div>
  </div>
  <div class="material abs" style="left:602px">
    <svg viewBox="0 0 230 240" aria-hidden="true">
      <g fill="var(--navy)">
        <rect x="8" y="8" width="64" height="64" rx="6"/><rect x="83" y="8" width="64" height="64" rx="6"/><rect x="158" y="8" width="64" height="64" rx="6"/>
        <rect x="8" y="88" width="64" height="64" rx="6"/><rect x="83" y="88" width="64" height="64" rx="6"/><rect x="158" y="88" width="64" height="64" rx="6"/>
        <rect x="8" y="168" width="64" height="64" rx="6"/><rect x="83" y="168" width="64" height="64" rx="6"/><rect x="158" y="168" width="64" height="64" rx="6"/>
      </g>
    </svg>
    <div class="material-label">TILE &amp; FLOORING</div>
  </div>
  <div class="material abs" style="left:900px">
    <svg viewBox="0 0 230 240" aria-hidden="true">
      <path d="M200 8 L222 30 L110 150 L88 128 Z" fill="var(--navy)"/>
      <path d="M82 136 L102 156 C96 196 60 222 8 226 C30 200 34 150 82 136 Z" fill="var(--navy)"/>
    </svg>
    <div class="material-label">FINISHES</div>
  </div>

  <h2 class="section-title pricing abs">Pricing Packages</h2>

  <div class="package package-minor abs">
    <div class="package-name">MINOR FINISH</div>
    <p class="package-desc">Gets the basement to the point of finished paint.</p>
    <ul class="features">
      <li><svg viewBox="0 0 10 10"><path d="M1 5 L4 8 L9 2" fill="none" stroke="#fff" stroke-width="1.8"/></svg>Framing</li>
      <li><svg viewBox="0 0 10 10"><path d="M1 5 L4 8 L9 2" fill="none" stroke="#fff" stroke-width="1.8"/></svg>Electrical Rough Ins</li>
      <li><svg viewBox="0 0 10 10"><path d="M1 5 L4 8 L9 2" fill="none" stroke="#fff" stroke-width="1.8"/></svg>Drywall</li>
      <li><svg viewBox="0 0 10 10"><path d="M1 5 L4 8 L9 2" fill="none" stroke="#fff" stroke-width="1.8"/></svg>Paint</li>
      <li><svg viewBox="0 0 10 10"><path d="M1 5 L4 8 L9 2" fill="none" stroke="#fff" stroke-width="1.8"/></svg>Trim &amp; Doors</li>
      <li><svg viewBox="0 0 10 10"><path d="M1 5 L4 8 L9 2" fill="none" stroke="#fff" stroke-width="1.8"/></svg>Flooring</li>
      <li><svg viewBox="0 0 10 10"><path d="M1 5 L4 8 L9 2" fill="none" stroke="#fff" stroke-width="1.8"/></svg>Plumbing Rough Ins</li>
      <li class="excluded"><svg viewBox="0 0 10 10"><path d="M1 5 L4 8 L9 2" fill="none" stroke="#fff" stroke-width="1.8"/></svg>Bathroom Addition</li>
      <li class="excluded"><svg viewBox="0 0 10 10"><path d="M1 5 L4 8 L9 2" fill="none" stroke="#fff" stroke-width="1.8"/></svg>Kitchen / Bar Addition</li>
      <li class="excluded"><svg viewBox="0 0 10 10"><path d="M1 5 L4 8 L9 2" fill="none" stroke="#fff" stroke-width="1.8"/></svg>Theater Room</li>
    </ul>
  </div>

  <div class="package package-moderate abs">
    <div class="package-name">MODERATE FINISH</div>
    <p class="package-desc">Typical basement finish, living space and bedroom with a bathroom.</p>
    <ul class="features">
      <li><svg viewBox="0 0 10 10"><path d="M1 5 L4 8 L9 2" fill="none" stroke="#fff" stroke-width="1.8"/></svg>Framing</li>
      <li><svg viewBox="0 0 10 10"><path d="M1 5 L4 8 L9 2" fill="none" stroke="#fff" stroke-width="1.8"/></svg>Electrical Rough Ins</li>
      <li><svg viewBox="0 0 10 10"><path d="M1 5 L4 8 L9 2" fill="none" stroke="#fff" stroke-width="1.8"/></svg>Drywall</li>
      <li><svg viewBox="0 0 10 10"><path d="M1 5 L4 8 L9 2" fill="none" stroke="#fff" stroke-width="1.8"/></svg>Paint</li>
      <li><svg viewBox="0 0 10 10"><path d="M1 5 L4 8 L9 2" fill="none" stroke="#fff" stroke-width="1.8"/></svg>Trim &amp; Doors</li>
      <li><svg viewBox="0 0 10 10"><path d="M1 5 L4 8 L9 2" fill="none" stroke="#fff" stroke-width="1.8"/></svg>Flooring</li>
      <li><svg viewBox="0 0 10 10"><path d="M1 5 L4 8 L9 2" fill="none" stroke="#fff" stroke-width="1.8"/></svg>Plumbing Rough Ins</li>
      <li><svg viewBox="0 0 10 10"><path d="M1 5 L4 8 L9 2" fill="none" stroke="#fff" stroke-width="1.8"/></svg>Bathroom Addition</li>
      <li class="excluded"><svg viewBox="0 0 10 10"><path d="M1 5 L4 8 L9 2" fill="none" stroke="#fff" stroke-width="1.8"/></svg>Kitchen / Bar Addition</li>
      <li class="excluded"><svg viewBox="0 0 10 10"><path d="M1 5 L4 8 L9 2" fill="none" stroke="#fff" stroke-width="1.8"/></svg>Theater Room</li>
    </ul>
  </div>

  <div class="package package-major abs">
    <div class="package-name">MAJOR FINISH</div>
    <p class="package-desc">Moderate finish plus a kitchen, bathroom and potentially theater.</p>
    <ul class="features">
      <li><svg viewBox="0 0 10 10"><path d="M1 5 L4 8 L9 2" fill="none" stroke="#fff" stroke-width="1.8"/></svg>Framing</li>
      <li><svg viewBox="0 0 10 10"><path d="M1 5 L4 8 L9 2" fill="none" stroke="#fff" stroke-width="1.8"/></svg>Electrical Rough Ins</li>
      <li><svg viewBox="0 0 10 10"><path d="M1 5 L4 8 L9 2" fill="none" stroke="#fff" stroke-width="1.8"/></svg>Drywall</li>
      <li><svg viewBox="0 0 10 10"><path d="M1 5 L4 8 L9 2" fill="none" stroke="#fff" stroke-width="1.8"/></svg>Paint</li>
      <li><svg viewBox="0 0 10 10"><path d="M1 5 L4 8 L9 2" fill="none" stroke="#fff" stroke-width="1.8"/></svg>Trim &amp; Doors</li>
      <li><svg viewBox="0 0 10 10"><path d="M1 5 L4 8 L9 2" fill="none" stroke="#fff" stroke-width="1.8"/></svg>Flooring</li>
      <li><svg viewBox="0 0 10 10"><path d="M1 5 L4 8 L9 2" fill="none" stroke="#fff" stroke-width="1.8"/></svg>Plumbing Rough Ins</li>
      <li><svg viewBox="0 0 10 10"><path d="M1 5 L4 8 L9 2" fill="none" stroke="#fff" stroke-width="1.8"/></svg>Bathroom Addition</li>
      <li><svg viewBox="0 0 10 10"><path d="M1 5 L4 8 L9 2" fill="none" stroke="#fff" stroke-width="1.8"/></svg>Kitchen / Bar Addition</li>
      <li><svg viewBox="0 0 10 10"><path d="M1 5 L4 8 L9 2" fill="none" stroke="#fff" stroke-width="1.8"/></svg>Theater Room</li>
    </ul>
  </div>

  <div class="best-value abs">BEST VALUE</div>
</body>
</html>
```